Velbrin Redesign of Website

I require my webpage to look different but this is out with my current providers platform
I will benefit from designs that use my wording (this is extremely important). I appreciate there may be a lot of wording in some areas so i would be happy with "read more" in various places. The use of my face in photo is a must and my logo is also a must which can be found on m y website www.velbrinadhd.co.uk I do not want corporate feel, i would like a warm, authentic. personal and inviting feel.

```html
<!DOCTYPE html>
<html lang="en">
<head>
<meta charset="utf-8">
<title>Velbrin – The Story Behind Velbrin</title>
<link href="https://fonts.googleapis.com/css2?family=Cormorant+Garamond:wght@500;600&family=Open+Sans:wght@700&family=Poppins:wght@400&family=Allura&display=swap" rel="stylesheet">
<style>
  :root {
    --cream: #f6f3ec;
    --forest: #0f3a30;
    --teal: #4a8293;
    --teal-text: #3f7b8c;
    --mist-blue: #c8d5de;
    --mist-blue-text: #5f8ea0;
    --white: #ffffff;
  }
  * { margin: 0; padding: 0; box-sizing: border-box; }
  html, body { width: 1200px; height: 675px; overflow: hidden; background: var(--cream); }
  .hero {
    position: relative;
    width: 1200px;
    height: 675px;
    overflow: hidden;
    background: var(--cream);
  }
  .hero__landscape {
    position: absolute;
    inset: 0;
    background:
      radial-gradient(ellipse 420px 260px at 560px 300px, rgba(170,170,120,0.28), transparent 70%),
      radial-gradient(ellipse 300px 360px at 1180px 420px, rgba(120,120,60,0.55), transparent 70%),
      linear-gradient(180deg, rgba(246,243,236,1) 0%, rgba(225,226,212,0.9) 35%, rgba(214,218,204,0.85) 55%, rgba(228,228,214,0.9) 75%, rgba(246,243,236,1) 100%);
  }
  .brand {
    position: absolute;
    left: 69px;
    top: 22px;
    width: 112px;
    display: flex;
    flex-direction: column;
    align-items: center;
    gap: 8px;
    z-index: 2;
  }
  .brand__mark {
    width: 72px;
    height: 72px;
    border: 2px solid var(--forest);
    border-radius: 50%;
  }
  .brand__name {
    font-family: "Cormorant Garamond", serif;
    font-weight: 600;
    font-size: 22px;
    letter-spacing: 2px;
    color: var(--forest);
  }
  .eyebrow {
    position: absolute;
    left: 69px;
    top: 168px;
    font-family: "Open Sans", sans-serif;
    font-weight: 700;
    font-size: 15px;
    color: var(--teal-text);
    letter-spacing: 0.2px;
    z-index: 2;
  }
  .headline {
    position: absolute;
    left: 63px;
    top: 196px;
    font-family: "Cormorant Garamond", serif;
    font-weight: 500;
    font-size: 92px;
    line-height: 92px;
    color: var(--forest);
    white-space: nowrap;
    z-index: 2;
  }
  .tagline {
    position: absolute;
    left: 66px;
    top: 396px;
    font-family: "Allura", cursive;
    font-size: 42px;
    line-height: 46px;
    color: var(--teal-text);
    z-index: 2;
  }
  .actions {
    position: absolute;
    left: 67px;
    top: 521px;
    display: flex;
    gap: 14px;
    z-index: 2;
  }
  .btn {
    display: inline-flex;
    align-items: center;
    justify-content: center;
    width: 232px;
    height: 47px;
    border-radius: 4px;
    font-family: "Poppins", sans-serif;
    font-size: 19px;
    text-decoration: none;
  }
  .btn--primary { background: var(--teal); color: var(--white); }
  .btn--secondary { background: var(--mist-blue); color: var(--mist-blue-text); }
  .portrait {
    position: absolute;
    left: 648px;
    top: 120px;
    width: 500px;
    height: 500px;
    z-index: 1;
  }
</style>
</head>
<body>
  <main class="hero">
    <div class="hero__landscape" role="img" aria-label="Misty lake surrounded by autumn forest and hills"></div>

    <div class="brand">
      <span class="brand__mark"></span>
      <span class="brand__name">VELBRIN</span>
    </div>

    <p class="eyebrow">ADHD COACHING AND WELLBEING</p>
    <h1 class="headline">The Story<br>Behind Velbrin</h1>
    <p class="tagline">Helping others began with<br>understanding myself.</p>

    <nav class="actions">
      <a class="btn btn--primary" href="#contact">Start A Conversation</a>
      <a class="btn btn--secondary" href="#approach">Explore The Approach</a>
    </nav>

    <svg class="portrait" viewBox="0 0 500 500" xmlns="http://www.w3.org/2000/svg">
      <defs>
        <linearGradient id="portraitTone" x1="0" y1="0" x2="0" y2="1">
          <stop offset="0" stop-color="#8a9a9c"/>
          <stop offset="0.45" stop-color="#c9b6a4"/>
          <stop offset="0.75" stop-color="#b8b9b6"/>
          <stop offset="1" stop-color="#1f4a4c"/>
        </linearGradient>
      </defs>
      <path fill="var(--mist-blue)" d="M110 100 C 150 40, 290 50, 390 60 C 470 70, 492 150, 492 220 C 496 300, 486 375, 420 432 C 350 492, 235 498, 165 452 C 98 408, 40 325, 8 250 C -10 190, 55 125, 110 100 Z"/>
      <g role="img" aria-label="Portrait of the coach by a lake">
        <path fill="url(#portraitTone)" d="M60 230 C 60 140, 125 20, 250 4 C 345 -6, 405 40, 435 100 C 455 160, 488 240, 483 318 C 478 385, 445 430, 388 458 C 320 492, 225 470, 168 432 C 110 394, 60 318, 60 230 Z"/>
      </g>
    </svg>
  </main>
</body>
</html>
```